Website for a Party Bus charter business

Please prepare a site for a local party bus charter company names Holloway Bus Company.
They hire a party bus, chatrer bus, boat hire and party trailer hire (place holder photos fine for these items).
I have included a wireframe design. This should be used, however creative licence is fully extended
Delivery of PSD is required and all fonts and source files
The client likes: http://www.tallquorin.com.au/ but must not look completely the same.
Should use a gold (simualr to #D1CFA1) colour, even if just background.
Updates
Hi All, just wondering if anyone is working on this as I have not received any responses or questions?
Is there anything I can do to assist?
Thanks all for the great submissions. I will be sending these onto the client today. Will let you know the outcome as soon as I can
Industry/Entity Type
Business
Look and feel
Each slider illustrates characteristics of the customer's brand and the style your logo design should communicate.

```html
<!DOCTYPE html>
<html lang="en">
<head>
<meta charset="utf-8">
<title>Holloway Bus Company – The Party Bus...Destination Fun</title>
<link href="https://fonts.googleapis.com/css2?family=Open+Sans:ital,wght@0,400;0,600;0,700;0,800;1,400&display=swap" rel="stylesheet">
<style>
:root{
  --gold:#d1cfa1;
  --gold-light:#f2f0d6;
  --cream:#f7f5e4;
  --olive:#8e8b5c;
  --olive-dark:#6d6b43;
  --navy:#0b0f3c;
  --ink:#1a1a3a;
  --muted:#55557a;
  --line:#b9b78c;
  --white:#ffffff;
  --sky:#1e8fd6;
}
*{box-sizing:border-box;margin:0;padding:0}
html,body{width:1200px;height:800px;overflow:hidden}
body{font-family:"Open Sans",Arial,sans-serif;color:var(--ink);background:var(--cream);position:relative}
.abs{position:absolute}
.photo{position:absolute;border-radius:1px}

/* header */
.site-header{left:0;top:0;width:1200px;height:32px;background:linear-gradient(#e9e7c8,#d8d6aa)}
.header-social{left:288px;top:1px;display:flex;gap:4px}
.header-social span{width:4px;height:4px;border-radius:50%;background:var(--muted)}
.brand{left:288px;top:6px;display:flex;align-items:center;gap:5px}
.brand-mark{width:9px;height:9px;border-radius:50%;background:var(--navy)}
.brand-name{font-weight:800;font-size:12.5px;color:var(--navy);letter-spacing:.2px;line-height:13px}
.tagline{left:350px;top:20px;font-weight:700;font-size:8.5px;line-height:10px;color:var(--navy)}
.contact{left:714px;top:1px;font-size:6.5px;line-height:8px;color:var(--ink);display:flex;gap:10px;align-items:center}
.contact i{display:inline-block;width:8px;height:5px;background:var(--navy);margin-right:3px;vertical-align:middle}
.contact i.ph{width:5px;height:5px;border-radius:50%;background:#c33}
.search{left:714px;top:11px;width:198px;height:9px;display:flex}
.search input{flex:1;border:1px solid var(--line);font:italic 5px "Open Sans",sans-serif;padding-left:3px;background:var(--white)}
.search button{width:30px;border:0;background:var(--navy)}
.main-nav{left:650px;top:22px;display:flex;gap:14px;font-size:6.5px;line-height:8px;align-items:center}
.main-nav .home{width:9px;height:7px;background:var(--navy)}

/* hero */
.hero{left:0;top:32px;width:1200px;height:193px;background:linear-gradient(#6b7a6c,#8a8a7c 55%,#a2a095)}
.hero-road{left:0;top:160px;width:1200px;height:65px;background:linear-gradient(#8c8c86,#b0aea2)}
.hero-main{left:288px;top:45px;width:624px;height:115px;background:radial-gradient(ellipse at 50% 45%,#b04fcf,#4a2a7a 55%,#1d1436)}
.hero-side-l1{left:75px;top:60px;width:75px;height:95px;background:linear-gradient(#c9d2c6,#8fa57a)}
.hero-side-l2{left:150px;top:50px;width:138px;height:105px;background:linear-gradient(#e8ecef,#9fb07e)}
.hero-side-r1{left:912px;top:52px;width:138px;height:105px;background:linear-gradient(#cfe0f0,#6f7f70)}
.hero-side-r2{left:1050px;top:60px;width:75px;height:95px;background:linear-gradient(#3a3a46,#8a7f55)}
.hero-edge-l{left:0;top:66px;width:75px;height:84px;background:linear-gradient(#6a5b78,#7c7a74)}
.hero-edge-r{left:1125px;top:66px;width:75px;height:84px;background:linear-gradient(#787a6a,#5d604f)}
.services{left:288px;top:175px;width:624px;display:flex;justify-content:space-between}
.service{width:93px;text-align:center}
.service h3{font-size:7px;line-height:9px;font-weight:700;color:var(--navy);margin-bottom:2px}
.service .thumb{height:33px;border:1px solid var(--white)}

/* intro */
.intro{left:0;top:225px;width:1200px;height:140px;background:linear-gradient(#fbfaf2,#f3f1e2)}
.sec-title{font-weight:800;font-size:11.5px;color:var(--navy);line-height:12px}
.sec-sub{font-style:italic;font-size:5.5px;line-height:6px;color:var(--muted)}
.offer{position:absolute;width:305px;height:32px}
.offer .thumb{position:absolute;left:0;top:0;width:93px;height:32px}
.offer h4{position:absolute;left:105px;top:-3px;width:200px;font-size:8.5px;line-height:12px;font-weight:800;color:var(--navy);border-bottom:1px solid var(--line);letter-spacing:.3px}
.offer p{position:absolute;left:105px;top:11px;width:200px;font-size:4.6px;line-height:1.12;font-style:italic;color:var(--ink)}
.offer .more{position:absolute;right:0;top:29px;font-size:4.3px;font-style:italic;font-weight:700;color:var(--navy)}

/* video band */
.video-band{left:0;top:365px;width:1200px;height:150px;background:radial-gradient(ellipse at 50% 50%,#b8b68a,var(--olive) 60%,var(--olive-dark))}
.video{left:290px;top:373px;width:624px;height:100px;background:linear-gradient(#8f918a,#5b5d58 60%,#3e3f3b)}
.play{left:580px;top:417px;width:52px;height:27px;border-radius:14px;border:2px solid var(--white);background:rgba(0,0,0,.2)}
.controls{left:288px;top:473px;width:626px;height:18px;background:linear-gradient(#5b5a52,#2e2d28);display:flex;align-items:center;font-size:6px;color:var(--white)}
.controls .cell{height:100%;border-right:1px solid #1e1d19;display:flex;align-items:center;justify-content:center}
.track{height:3px;background:#cfcfc4;border-radius:2px}
.video-caption{left:288px;top:492px;width:230px}
.video-caption h5{font-size:7px;line-height:9px;font-weight:700;color:var(--navy)}
.video-caption p{font-size:4.2px;color:var(--white);line-height:1.15}
.arrows{left:880px;top:497px;font-size:11px;color:var(--ink);display:flex;gap:14px}
.arrows .dim{color:var(--gold-light)}

/* coast */
.coast{left:0;top:515px;width:1200px;height:182px;background:linear-gradient(var(--gold-light),#e4e2bd)}
.coast-photo{left:288px;top:542px;width:305px;height:70px;background:linear-gradient(#b7c4cf,#cfd0c8 45%,#8e877a 65%,#c7b79a)}
.coast-copy{left:607px;top:538px;width:306px;font-size:5.5px;line-height:1.18;color:var(--ink)}
.coast-copy p{margin-bottom:4px}
.btn{position:absolute;background:var(--navy);color:var(--white);font-weight:700;text-align:center;letter-spacing:.5px}
.tweets{left:288px;top:618px;width:305px;height:73px;background:var(--white)}
.tweets-head{height:14px;background:var(--sky);color:var(--white);position:relative}
.tweets-head .dot{position:absolute;left:6px;top:2px;width:10px;height:10px;border-radius:50%;background:var(--white)}
.tweets-head b{position:absolute;left:45px;top:0;font-size:8.5px;line-height:9px;font-weight:600}
.tweets-head small{position:absolute;left:48px;top:9px;font-size:4.5px;line-height:5px}
.tweets-head .follow{position:absolute;right:0;top:0;height:14px;padding:0 12px;font-size:9px;font-weight:600;line-height:14px;border-left:1px solid #5ab0e6}
.tweet{position:absolute;left:4px;width:293px;height:17px;font-size:5.5px;line-height:6px}
.tweet .av{position:absolute;left:0;top:2px;width:40px;height:12px;background:linear-gradient(#d6a850,#5a4a6a)}
.tweet .txt{position:absolute;left:48px;top:0}
.tweet .meta{position:absolute;left:48px;top:12px;width:245px;font-size:4.8px;line-height:5px;color:#aaa;display:flex;justify-content:space-between}
.find-us{left:732px;top:620px;font-size:8.5px;line-height:10px;font-weight:800;color:var(--navy)}
.map{left:612px;top:632px;width:300px;height:58px;background:linear-gradient(135deg,#dbe7f1,#b9d3e3 55%,#8fb3c9)}

/* footer columns */
.footer-cols{left:0;top:697px;width:1200px;height:83px;background:linear-gradient(#fbf9e6,#f1efd4)}
.col-title{position:absolute;font-weight:800;font-size:11px;line-height:11px;color:var(--navy)}
.small-txt{position:absolute;font-size:5.2px;line-height:6px;font-style:italic}
.news-thumb{position:absolute;width:52px;height:18px;background:linear-gradient(135deg,#9fd3f5,#1f7fcf)}
.field{position:absolute;left:713px;width:199px;height:9px;background:var(--gold);font-size:5px;color:var(--white);padding-left:10px;line-height:9px}

/* bottom bar */
.bottom-bar{left:0;top:780px;width:1200px;height:20px;background:var(--gold);font-size:5px;line-height:6px;color:var(--ink)}
.foot-social{position:absolute;top:7px;width:9px;height:9px;border-radius:50%}
</style>
</head>
<body>

<header class="abs site-header">
  <div class="abs header-social"><span></span><span></span><span></span><span></span></div>
  <div class="abs brand"><span class="brand-mark"></span><span class="brand-name">Holloway Bus Company</span></div>
  <div class="abs tagline">The Party Bus...Destination Fun</div>
  <div class="abs contact"><span><i></i>hello@hollowaycoaches.com</span><span><i class="ph"></i>0400-555-217</span></div>
  <form class="abs search"><input type="text" placeholder="Search for vehicles here..."><button type="button" aria-label="Search"></button></form>
  <nav class="abs main-nav"><span class="home"></span><span>About Us</span><span>Buses</span><span>Gallery</span><span>Get a Quote</span><span>Contact</span></nav>
</header>

<section class="abs hero"></section>
<div class="abs hero-road" role="img" aria-label="Blurred road backdrop behind the slider"></div>
<div class="photo hero-edge-l" role="img" aria-label="Party bus side view"></div>
<div class="photo hero-side-l1" role="img" aria-label="Painted party bus at a campsite"></div>
<div class="photo hero-side-l2" role="img" aria-label="Family relaxing beside a house bus"></div>
<div class="photo hero-main" role="img" aria-label="Party bus interior lit in purple with guests dancing"></div>
<div class="photo hero-side-r1" role="img" aria-label="Guests on the deck of a party boat"></div>
<div class="photo hero-side-r2" role="img" aria-label="Custom built bus at night"></div>
<div class="photo hero-edge-r" role="img" aria-label="Bus on a coastal road"></div>

<div class="abs services">
  <div class="service"><h3>Party Bus</h3><div class="thumb photo" style="position:relative;background:linear-gradient(#7a3fb0,#2a1648)" role="img" aria-label="Party bus interior"></div></div>
  <div class="service"><h3>Charter Bus</h3><div class="thumb photo" style="position:relative;background:linear-gradient(#9cc6e8,#c28a46)" role="img" aria-label="Charter coach"></div></div>
  <div class="service"><h3>Party Trailer</h3><div class="thumb photo" style="position:relative;background:linear-gradient(#5fb7c9,#d44a3a)" role="img" aria-label="Party trailer"></div></div>
  <div class="service"><h3>Party Boat</h3><div class="thumb photo" style="position:relative;background:linear-gradient(#a8d0ea,#e88a3a)" role="img" aria-label="Party boat"></div></div>
  <div class="service"><h3>House Bus</h3><div class="thumb photo" style="position:relative;background:linear-gradient(#e6ecef,#8fb06a)" role="img" aria-label="House bus campsite"></div></div>
  <div class="service"><h3>Want Your Own</h3><div class="thumb photo" style="position:relative;background:linear-gradient(#2b2b44,#b08a3a)" role="img" aria-label="Custom bus build"></div></div>
</div>

<section class="abs intro"></section>
<div class="abs" style="left:288px;top:232px">
  <h2 class="sec-title">Holloway Bus Company</h2>
  <p class="sec-sub">Lorem ipsum dolor sit amet, consectetur adipisicing</p>
</div>

<article class="offer" style="left:288px;top:252px"><div class="thumb" style="background:linear-gradient(#7a3fb0,#2a1648)" role="img" aria-label="Party bus interior"></div><h4>Party Bus</h4><p>Lorem ipsum dolor sit amet, r adipisicing elit, sed do eiusmod tempor incididunt ut labore et dolore magna aliqua. Ut enim ad minim veniam, quis nostrud exercitation ullamco laboris nisi ut aliquip ex ea commodo consequat. Duis aute irure dolor in reprehenderit in voluptate velit esse cillum</p><span class="more">Read more...</span></article>
<article class="offer" style="left:288px;top:290px"><div class="thumb" style="background:linear-gradient(#9cc6e8,#c28a46)" role="img" aria-label="Charter coach"></div><h4>Charter Bus</h4><p>Lorem ipsum dolor sit amet, r adipisicing elit, sed do eiusmod tempor incididunt ut labore et dolore magna aliqua. Ut enim ad minim veniam, quis nostrud exercitation ullamco laboris nisi ut aliquip ex ea commodo consequat. Duis aute irure dolor in reprehenderit in voluptate velit esse cillum</p><span class="more">Read more...</span></article>
<article class="offer" style="left:288px;top:328px"><div class="thumb" style="background:linear-gradient(#5fb7c9,#d44a3a)" role="img" aria-label="Party trailer"></div><h4>Party Trailer</h4><p>Lorem ipsum dolor sit amet, r adipisicing elit, sed do eiusmod tempor incididunt ut labore et dolore magna aliqua. Ut enim ad minim veniam, quis nostrud exercitation ullamco laboris nisi ut aliquip ex ea commodo consequat. Duis aute irure dolor in reprehenderit in voluptate velit esse cillum</p><span class="more">Read more...</span></article>
<article class="offer" style="left:607px;top:252px"><div class="thumb" style="background:linear-gradient(#a8d0ea,#e88a3a)" role="img" aria-label="Party boat"></div><h4>Party Boat</h4><p>Lorem ipsum dolor sit amet, r adipisicing elit, sed do eiusmod tempor incididunt ut labore et dolore magna aliqua. Ut enim ad minim veniam, quis nostrud exercitation ullamco laboris nisi ut aliquip ex ea commodo consequat. Duis aute irure dolor in reprehenderit in voluptate velit esse cillum</p><span class="more">Read more...</span></article>
<article class="offer" style="left:607px;top:290px"><div class="thumb" style="background:linear-gradient(#e6ecef,#8fb06a)" role="img" aria-label="House bus at a campsite"></div><h4>House Bus</h4><p>Lorem ipsum dolor sit amet, r adipisicing elit, sed do eiusmod tempor incididunt ut labore et dolore magna aliqua. Ut enim ad minim veniam, quis nostrud exercitation ullamco laboris nisi ut aliquip ex ea commodo consequat. Duis aute irure dolor in reprehenderit in voluptate velit esse cillum</p><span class="more">Read more...</span></article>
<article class="offer" style="left:607px;top:328px"><div class="thumb" style="background:linear-gradient(#2b2b44,#b08a3a)" role="img" aria-label="Custom bus build"></div><h4>Want Your Own</h4><p>Lorem ipsum dolor sit amet, r adipisicing elit, sed do eiusmod tempor incididunt ut labore et dolore magna aliqua. Ut enim ad minim veniam, quis nostrud exercitation ullamco laboris nisi ut aliquip ex ea commodo consequat. Duis aute irure dolor in reprehenderit in voluptate velit esse cillum</p><span class="more">Read more...</span></article>

<section class="abs video-band"></section>
<div class="photo video" role="img" aria-label="Vintage van parked on a city street, video still"></div>
<div class="abs play"><svg width="48" height="23" viewBox="0 0 48 23"><polygon points="20,5 31,11.5 20,18" fill="#fff"/></svg></div>
<div class="abs controls">
  <div class="cell" style="width:62px"><svg width="6" height="7"><rect x="0" y="0" width="2" height="7" fill="#fff"/><rect x="4" y="0" width="2" height="7" fill="#fff"/></svg></div>
  <div class="cell" style="width:350px;justify-content:flex-start;padding:0 8px;gap:12px"><div class="track" style="width:255px"></div><span>33:46 / 59:03</span></div>
  <div class="cell" style="width:110px;gap:8px"><svg width="6" height="6"><polygon points="0,2 2,2 5,0 5,6 2,4 0,4" fill="#fff"/></svg><div class="track" style="width:80px"></div></div>
  <div class="cell" style="width:42px;font-weight:700">HD</div>
  <div class="cell" style="width:60px;border:0">⤢</div>
</div>
<div class="abs video-caption">
  <h5>Vintage fun</h5>
  <p>Take a ride in our classic kombi, restored with care for weddings and road trips along the coast.<br>4 days ago</p>
</div>
<div class="abs arrows"><span class="dim">‹</span><span>›</span></div>

<section class="abs coast"></section>
<div class="abs" style="left:288px;top:519px">
  <h2 class="sec-title">Best Way to See the Coast</h2>
  <p class="sec-sub">Lorem ipsum dolor sit amet, consectetur adipisicing elit, sed do</p>
</div>
<div class="photo coast-photo" role="img" aria-label="Beach and sea under a cloudy sky"></div>
<div class="abs coast-copy">
  <p>Lorem ipsum dolor sit amet, consectetur adipisicing elit, sed do eiusmod tempor incididunt ut labore et dolore magna aliqua. Ut enim ad minim veniam, quis nostrud exercitation ullamco laboris nisi ut aliquip ex ea commodo consequat.</p>
  <p>Duis aute irure dolor in reprehenderit in voluptate velit esse cillum dolore eu fugiat nulla pariatur. Excepteur sint occaecat cupidatat non proident, sunt in culpa qui officia deserunt mollit anim id est laborum.</p>
  <p>Sed ut perspiciatis unde omnis iste natus error sit voluptatem accusantium doloremque laudantium, totam rem aperiam, eaque ipsa quae ab illo inventore veritatis et quasi architecto beatae vitae dicta sunt explicabo. Nemo enim ipsam voluptatem quia voluptas sit aspernatur aut odit aut fugit, sed quia consequuntur magni dolores eos qui ratione voluptatem sequi nesciunt. Neque porro quisquam est, qui dolorem ipsum quia dolor</p>
</div>
<a class="btn" style="left:766px;top:602px;width:147px;height:10px;font-size:8px;line-height:10px">Book it Now</a>

<div class="abs tweets">
  <div class="tweets-head"><span class="dot"></span><b>Tweets</b><small>Our Feed</small><span class="follow">Follow Us</span></div>
  <div class="tweet" style="top:17px"><span class="av"></span><span class="txt"><b>Holloway Bus</b> <span style="color:#aaa">@hollowaybus · 3m</span><br>Experience more fun with extended party tours http://hw.me/1m</span><span class="meta"><span>Expand</span><span>Reply · Retweet · Favorite · More</span></span></div>
  <div class="tweet" style="top:35px"><span class="av"></span><span class="txt"><b>Holloway Bus</b> <span style="color:#aaa">@hollowaybus · 5m</span><br>Experience more fun with extended party tours http://hw.me/1m</span><span class="meta"><span>Expand</span><span>Reply · Retweet · Favorite · More</span></span></div>
  <div class="tweet" style="top:53px"><span class="av"></span><span class="txt"><b>Holloway Bus</b> <span style="color:#aaa">@hollowaybus · 8m</span><br>Experience more fun with extended party tours http://hw.me/1m</span><span class="meta"><span>Expand</span><span>Reply · Retweet · Favorite · More</span></span></div>
</div>

<div class="abs find-us">Find Us</div>
<div class="photo map" role="img" aria-label="Folded world map marking the depot location"></div>

<section class="abs footer-cols"></section>
<h3 class="col-title" style="left:287px;top:700px">Prices &amp; Bookings</h3>
<div class="photo" style="left:288px;top:713px;width:75px;height:28px;background:linear-gradient(135deg,#9fd3f5,#1f7fcf)" role="img" aria-label="Booking agent illustration"></div>
<p class="small-txt" style="left:368px;top:713px;width:110px">Lorem ipsum dolor sit amet, ing elit, sed do eiusmod on cidnt ut labore et dolore magna aliqua.<br>Ut enim ad minim veniam, strud exercitation ullamco</p>
<a class="btn" style="left:328px;top:745px;width:119px;height:10px;font-size:8px;line-height:10px">Get a Quote</a>
<span class="abs" style="left:385px;top:757px;font-size:5px;line-height:6px">or</span>
<a class="btn" style="left:328px;top:766px;width:119px;height:10px;font-size:8px;line-height:10px">Book Now</a>

<h3 class="col-title" style="left:500px;top:700px">Latest News</h3>
<div class="news-thumb" style="left:500px;top:713px" role="img" aria-label="News image"></div>
<p class="small-txt" style="left:560px;top:713px;width:140px">Lorem ipsum dolor sit amet, ing elit, sed do eiusmod on cidnt ut labore et dolore magna aliqua.<br>Ut enim ad minim veniam, strud station <b style="float:right">Read more...</b></p>
<div class="news-thumb" style="left:500px;top:735px" role="img" aria-label="News image"></div>
<p class="small-txt" style="left:560px;top:735px;width:140px">Lorem ipsum dolor sit amet, ing elit, sed do eiusmod on cidnt ut labore et dolore magna aliqua.<br>Ut enim ad minim veniam, strud station <b style="float:right">Read more...</b></p>
<div class="news-thumb" style="left:500px;top:757px" role="img" aria-label="News image"></div>
<p class="small-txt" style="left:560px;top:757px;width:140px">Lorem ipsum dolor sit amet, ing elit, sed do eiusmod on cidnt ut labore et dolore.<br>Ut enim ad minim veniam, strud station <b style="float:right">Read more...</b></p>

<h3 class="col-title" style="left:713px;top:700px">Join Our VIP Club</h3>
<p class="small-txt" style="left:713px;top:712px;width:199px">Lorem ipsum dolor sit amet, ing elit, sed do eiusmod on cidnt ut labore et dolore magna aliqua.</p>
<div class="field" style="top:725px">Your Name</div>
<div class="field" style="top:739px">Your Phone Number* <span style="float:right;margin-right:4px;color:var(--ink);font-style:italic">*Optional</span></div>
<div class="field" style="top:753px">Your Email Address</div>
<a class="btn" style="left:713px;top:766px;width:199px;height:10px;font-size:7.5px;line-height:10px">Get Access The VIP Club Now</a>

<footer class="abs bottom-bar">
  <span class="abs" style="left:288px;top:7px">Copyright © 2014 Holloway Bus Company</span>
  <span class="abs" style="left:592px;top:7px">Privacy Policy</span>
  <span class="abs" style="left:652px;top:7px">Terms &amp; Conditions</span>
  <span class="foot-social" style="left:810px;background:#3b5998"></span>
  <span class="foot-social" style="left:840px;background:var(--sky)"></span>
  <span class="foot-social" style="left:870px;background:#d44a3a"></span>
  <span class="foot-social" style="left:900px;background:#c0283a"></span>
</footer>

</body>
</html>
```